Hair salon and Nail salon in Hawaii need a newspaper Ad design.

We need a newspaper Ad design for new open hair & nail salon in Waikiki Hawaii.Our Recommendation service for hair is "Head Spa" $30+tax and for nail is "Manicure Treatment Course" (Filing+Cuticle Care+Massage+Coloring) $20+tax.
We would like to see Hawaiian taste color and also having sense of luxury design. The ad size is W 5.0” x H 6.375”.
I would customers to know the shop place(Palisade Crestway Hotel 1F) , phone(808-555-0172), instagram(salonvelmara) , our web site https://salonvelmara.example and recommend services. For Web or Instagram , QR code is acceptable.

Target Market(s)

women & men

Industry/Entity Type

Beauty Salon

Font styles to use
Serif

Colors

Designer to choose colors to be used in the design.

Requirements
Must have
• Tagline for local customers. Shop Name is "SALON VELMARA".the shop place(Palisade Crestway Hotel 1F) , phone(808-555-0172), instagram(salonvelmara) and recommend services.
Nice to have
• Our services are competitive, but we don't want to be seen as just cheap and low quality.

```html
<!DOCTYPE html>
<html lang="en">
<head>
<meta charset="utf-8">
<title>Salon Velmara – Newspaper Ad</title>
<link rel="stylesheet" href="https://fonts.googleapis.com/css2?family=Kaushan+Script&family=PT+Serif&family=Ubuntu:ital,wght@0,400;0,500;0,700;1,400&family=Cabin:wght@500&display=swap">
<style>
  :root{
    --cream:#ecdcbd;
    --sand:#d9bf95;
    --cocoa:#4a2c16;
    --rule:#9b4b2c;
    --band-dark:#3a2a1b;
    --band-warm:#a96c33;
    --gold:#c9a46a;
    --gold-line:#b88443;
    --ivory:#f2e6d2;
    --white:#ffffff;
  }
  *{margin:0;padding:0;box-sizing:border-box}
  html,body{width:1200px;height:941px;overflow:hidden;background:#fff}
  .ad{
    position:relative;width:1200px;height:941px;overflow:hidden;
    background:linear-gradient(100deg,#7a5a3e 0%,#a9865f 28%,#cdb08a 46%,var(--cream) 72%,#e6d2ae 100%);
  }
  .portrait{
    position:absolute;left:-80px;top:-60px;width:860px;height:880px;
    background:
      radial-gradient(ellipse 38% 30% at 30% 22%,rgba(92,58,34,.85) 0%,rgba(92,58,34,0) 100%),
      radial-gradient(ellipse 30% 34% at 40% 56%,rgba(176,122,82,.9) 0%,rgba(176,122,82,0) 100%),
      radial-gradient(ellipse 55% 60% at 35% 45%,rgba(110,69,41,.75) 0%,rgba(110,69,41,.35) 55%,rgba(110,69,41,0) 100%);
  }
  .headline{font-family:"Kaushan Script",cursive;color:var(--cocoa);position:absolute;white-space:nowrap;transform-origin:0 100%;transform:rotate(-13deg);line-height:1}
  .headline--lead{left:459px;top:122px;font-size:48px}
  .headline--main{left:522px;top:168px;font-size:80px}
  .swoosh{position:absolute;left:0;top:0}
  .menu{position:absolute;left:563px;top:300px;width:530px;font-family:"PT Serif",serif;color:var(--cocoa)}
  .menu__row{display:flex;position:relative}
  .menu__name{width:314px;font-size:45px;line-height:47px;text-transform:uppercase}
  .menu__price{padding-left:22px;font-size:45px;line-height:47px;border-left:2px solid var(--rule)}
  .menu__row--spa{padding-bottom:12px;margin-bottom:14px}
  .menu__row--spa::after{content:"";position:absolute;left:0;bottom:0;width:300px;border-bottom:2px solid var(--rule)}
  .menu__row--spa::before{content:"";position:absolute;left:327px;bottom:0;width:198px;border-bottom:2px solid var(--rule)}
  .menu__price--spa{height:50px}
  .menu__price--manicure{height:96px}
  .menu__detail{font-family:"Ubuntu",sans-serif;font-size:28px;line-height:33px;margin-top:-2px}
  .band{position:absolute;left:0;top:0}
  .nail-photo{
    position:absolute;left:858px;top:496px;width:292px;height:292px;border-radius:50%;
    background:radial-gradient(circle at 55% 45%,#f4ece6 0%,#e6d3c7 45%,#b9b6c4 78%,#8a8a98 100%);
    box-shadow:0 14px 24px rgba(40,25,10,.45);
  }
  .social{position:absolute;left:51px;top:748px;display:flex;align-items:center;font-family:"Ubuntu",sans-serif;font-size:24px;color:var(--ivory);gap:10px}
  .social__dot{width:24px;height:24px;border:2px solid var(--gold);border-radius:50%}
  .social__web{margin-left:14px;display:flex;align-items:center;gap:10px}
  .brand{position:absolute;left:50px;top:785px;font-family:"Cabin",sans-serif;font-weight:500;font-size:62px;line-height:1;color:var(--gold);letter-spacing:1px}
  .tagline{position:absolute;left:0;width:690px;top:860px;text-align:center;font-family:"Ubuntu",sans-serif;font-style:italic;font-size:31px;color:var(--ivory)}
  .contact{position:absolute;left:693px;top:810px;font-family:"Ubuntu",sans-serif;font-style:normal;color:var(--white)}
  .contact__place{font-size:33px;line-height:40px}
  .contact__phone{font-size:43px;line-height:52px;font-weight:700}
</style>
</head>
<body>
<main class="ad">
  <div class="portrait" role="img" aria-label="Portrait photo of a smiling woman with voluminous curly hair"></div>

  <p class="headline headline--lead">Are you ready for a</p>
  <p class="headline headline--main">New &amp; Better you?</p>
  <svg class="swoosh" width="1200" height="941" aria-hidden="true">
    <path d="M605 284 C700 230 820 195 950 172 C830 200 720 238 618 282 Z" fill="var(--cocoa)"/>
  </svg>

  <section class="menu">
    <div class="menu__row menu__row--spa">
      <span class="menu__name">Head Spa</span>
      <span class="menu__price menu__price--spa">$30+Tax</span>
    </div>
    <div class="menu__row">
      <span class="menu__name">Manicure<br>Treatment<br>Course</span>
      <span class="menu__price menu__price--manicure">$20+Tax</span>
    </div>
    <p class="menu__detail">(Filing+Cuticle Care<br>+Massage+Coloring)</p>
  </section>

  <svg class="band" width="1200" height="941" aria-hidden="true">
    <defs>
      <linearGradient id="bandFill" x1="0" y1="0" x2="1" y2="0">
        <stop offset="0" stop-color="var(--band-dark)"/>
        <stop offset="0.5" stop-color="#5e3b20"/>
        <stop offset="1" stop-color="var(--band-warm)"/>
      </linearGradient>
    </defs>
    <path d="M1120 540 C1160 515 1185 492 1200 466 L1200 486 C1180 510 1150 532 1120 548 Z" fill="#6a4220"/>
    <path d="M0 625 C260 720 720 735 1200 480 L1200 941 L0 941 Z" fill="url(#bandFill)"/>
    <path d="M0 616 C260 712 720 727 1200 472" fill="none" stroke="var(--gold-line)" stroke-width="5"/>
  </svg>

  <div class="nail-photo" role="img" aria-label="Photo of manicured hands with dark nail polish, spa stones and a polish bottle"></div>

  <div class="social">
    <span class="social__dot" aria-hidden="true"></span>
    <span>@salonvelmara</span>
    <span class="social__web">
      <svg width="24" height="32" viewBox="0 0 24 32" aria-hidden="true"><path d="M2 2 L2 26 L8 20 L12 30 L16 28 L12 18 L20 18 Z" fill="var(--gold)"/></svg>
      <span>salonvelmara.example</span>
    </span>
  </div>

  <h1 class="brand">SALON VELMARA</h1>
  <p class="tagline">“Quality Care, Quality Hair”</p>

  <address class="contact">
    <p class="contact__place">Palisade Crestway Hotel 1F</p>
    <p class="contact__phone">Call: 808-555-0172</p>
  </address>
</main>
</body>
</html>
```